Thoroughbred Racing Partnership needs web design

Crest of Fortune Partners is a management group who buys horses and races them on both the West and East coasts. The premise of the business is for an investment as little as $500, anyone can be a partner and own a percentage of a horse(s). This is a low cost way of getting involved in the exciting sport of Thoroughbred Racing, without shouldering the heavy financial responsibility. Our target market is mostly males 40+ but we want to include all target markets. We are looking for something very clean and professional, we want to give an image of success. Nothing overly "artsy." I have included the logo in which you can incorporate in the site. Also, the logo colors will be the colors of our "silks." The silks are what the jockey wears and will be an important marketing tool for COF. We would like a very prominent picture of a racehorse somewhere on the homepage, we want to make it clear that is a website for Horseracing partnerships.

On the top of the site, it should say "Crest of Fortune" (on the top)
and below that "Thoroughbred Racing Partnerships." (below that)

The main sections, which should be across the top are:

Home
About Us
Ownership
Stable Roster
News
Contact us

Some of these will have drop down menus.

An example of a competitor website that we like is: www.harlowfieldeq.example
An example of a competitor website that we don't like is: www.gallopvane.example
Updates

Project Deadline Extended
Reason: We have a Board of Directors meeting on the 22nd and we will be making a decision on that day. I'm giving an extension so that all designers are able to submit their designs by the 22nd. Thank you!

Target Market(s)

40+ males

Industry/Entity Type

Business

Requirements
Must have
• our logo must be on the site. We would like at least one bold image of a thoroughbred horse in action. The picture is going to tell the story so it needs to be very eye-catching.

Our slogan should also be included on the website, "Experience the thrill of owning a Racehorse."
Should not have
• cartoons, artsy pictures, pictures of Steeplechase horses or "jumpers." This partnership is for racehorses only, there is not jumping involved with the horses.

```html
<!DOCTYPE html>
<html lang="en">
<head>
<meta charset="utf-8">
<title>Crest of Fortune – Thoroughbred Racing Partnerships</title>
<link href="https://fonts.googleapis.com/css2?family=Ubuntu:wght@300;400;500&family=Oswald:wght@300;400&family=Arimo:wght@400;700&display=swap" rel="stylesheet">
<style>
:root{
  --page:#eef3f8;
  --panel:#f7f9fb;
  --navy:#0b2d5e;
  --hero-navy:#0a2a5c;
  --heading:#0e4f80;
  --nav-top:#a3cbe2;
  --nav-bottom:#6ea6c8;
  --nav-active:#4a7fa7;
  --text:#555b61;
  --date:#5d6268;
  --link:#4169e1;
  --footer-link:#1a2fa0;
  --button:#0d5588;
  --rule:#c6dcec;
  --social:#b4b8bc;
  --social-light:#c9cccf;
}
*{margin:0;padding:0;box-sizing:border-box}
html,body{width:917px;height:1200px;overflow:hidden}
body{background:var(--page);position:relative;font-family:"Arimo",Arial,sans-serif;color:var(--text)}
.abs{position:absolute}

.brand{left:67px;top:20px;display:flex;align-items:center;gap:8px;font-family:"Ubuntu",sans-serif;font-weight:500;font-size:19px;color:var(--navy);line-height:1.05}
.brand-mark{width:40px;height:40px;border-radius:50%;background:var(--navy)}
.site-title{left:0;width:952px;top:22px;text-align:center;font-family:"Ubuntu",sans-serif}
.site-title h1{font-size:25px;font-weight:500;color:var(--navy);letter-spacing:.3px}
.site-title p{font-size:16.5px;font-weight:300;color:var(--heading);margin-top:-2px}
.social{display:flex;gap:4px}
.social span{width:25px;height:25px;border-radius:50%;display:block;background:radial-gradient(circle at 40% 35%,var(--social-light),var(--social) 70%);box-shadow:inset 0 0 0 1px rgba(255,255,255,.35)}
.social.top{left:733px;top:51px}
.social.bottom{left:734px;top:1120px}

.main-nav{left:0;top:94px;width:917px;height:31px;background:linear-gradient(var(--nav-top),var(--nav-bottom));border-top:1px solid #d7e8f3;border-bottom:1px solid #d7e8f3}
.main-nav a{position:absolute;top:0;height:29px;line-height:29px;font-family:"Ubuntu",sans-serif;font-weight:300;font-size:15px;color:#fff;text-decoration:none}
.main-nav a.active{background:var(--nav-active);padding:0 19px;left:65px}

.hero{left:0;top:125px;width:917px;height:307px;background:var(--hero-navy);overflow:hidden}
.hero-photo{position:absolute;left:0;top:0;width:820px;height:307px;
  background:
    linear-gradient(180deg,rgba(150,175,205,.55) 0%,rgba(150,175,205,0) 30%,rgba(0,0,0,0) 72%,rgba(96,140,60,.85) 86%,rgba(190,120,120,.8) 100%),
    linear-gradient(90deg,#5a3a2e 0%,#8a4a2a 14%,#b0562e 30%,#c8463e 40%,#a9532c 52%,#8e4a2a 62%,#6d6a5a 72%);
  -webkit-mask-image:linear-gradient(90deg,rgba(0,0,0,.55) 0%,#000 10%,#000 62%,transparent 88%);
  mask-image:linear-gradient(90deg,rgba(0,0,0,.55) 0%,#000 10%,#000 62%,transparent 88%)}
.slogan{position:absolute;left:606px;top:93px;font-family:"Oswald",sans-serif;font-weight:400;color:#fff;line-height:1;letter-spacing:-.6px}
.slogan .l1{font-size:40px;display:block}
.slogan .l2{font-size:28px;display:block;margin-top:10px}
.slogan .l2 b{font-weight:400;font-size:40px}
.slogan .l3{font-size:28px;display:block;margin-top:6px}
.slogan .l3 b{font-weight:400;font-size:44px}

.dots{left:425px;top:438px;display:flex;gap:6px;align-items:center}
.dots span{width:11px;height:11px;border-radius:50%;background:#3b3f4a}
.dots span.on{width:13px;height:13px;background:#1238c2}

.panel{left:65px;top:479px;width:783px;height:615px;background:var(--panel);border-radius:6px}
h2{position:absolute;font-family:"Ubuntu",sans-serif;font-weight:400;font-size:19px;color:var(--heading);letter-spacing:.2px}
.copy{position:absolute;font-size:10px;line-height:16.7px}
.btn{position:absolute;height:18px;line-height:18px;background:var(--button);color:#fff;font-size:10px;text-align:center;text-decoration:none;box-shadow:0 0 0 1px #d7e4ee}
.photo{position:absolute;border:2px solid #fff;box-shadow:0 0 3px rgba(0,0,0,.35)}
.photo.owners{left:679px;top:524px;width:143px;height:107px;background:linear-gradient(135deg,#2b2a2e,#6b5a52 50%,#2c3a66)}
.photo.race{left:104px;top:743px;width:198px;height:149px;background:linear-gradient(150deg,#c7a89c,#9d4f2a 45%,#5a2c1a 100%)}
.hrule{left:65px;top:687px;width:783px;height:1px;background:var(--rule)}
.vrule{left:457px;top:710px;width:1px;height:351px;background:var(--rule)}

.news-item{position:absolute;left:493px;width:250px}
.news-item h3{font-size:14px;font-weight:700;color:var(--date);margin-bottom:3px}
.news-item p{font-size:10px;line-height:16.7px}
.news-item a{font-size:10px;color:var(--link);text-decoration:none;display:block;margin-top:-1px}

.footer-nav{left:67px;top:1119px;font-size:10px;color:var(--footer-link)}
.footer-nav a{color:var(--footer-link);text-decoration:none}
.footer-nav i{font-style:normal;margin:0 5px}
.copyright{left:65px;top:1140px;font-family:"Ubuntu",sans-serif;font-size:10.5px;color:var(--footer-link)}
</style>
</head>
<body>

<header>
  <div class="brand abs"><span class="brand-mark"></span><span>COF<br>PARTNERS.COM</span></div>
  <div class="site-title abs"><h1>Crest of Fortune</h1><p>Thoroughbred Racing Partnerships</p></div>
  <div class="social top abs"><span></span><span></span><span></span><span></span></div>
</header>

<nav class="main-nav abs">
  <a class="active" href="#">Home</a>
  <a href="#" style="left:169px">About Us</a>
  <a href="#" style="left:275px">Ownership</a>
  <a href="#" style="left:392px">Stable Roster</a>
  <a href="#" style="left:528px">News</a>
  <a href="#" style="left:609px">Contact us</a>
</nav>

<section class="hero abs">
  <div class="hero-photo" role="img" aria-label="Jockey in red silks riding a chestnut thoroughbred at full gallop past the flower-lined rail"></div>
  <p class="slogan"><span class="l1">Experience</span><span class="l2">the thrill of <b>owning</b></span><span class="l3">a <b>Racehorse</b></span></p>
</section>

<div class="dots abs"><span></span><span class="on"></span><span></span><span></span></div>

<main class="panel abs"></main>

<h2 style="left:103px;top:519px">WHY A HORSE RACING PARTNERSHIP WITH US?</h2>
<p class="copy" style="left:103px;top:565px;width:556px">Lorem ipsum dolor sit amet, consectetur adipiscing elit. Curabitur eget nibh id enim laoreet euismod eget ac orci. Vestibulum anipsum primis in faucibus orci luctus. et ultrices posuere cubilia Curae; Cras pellentesque euismod fringilla. Sed vitae ante lectus, non fringilla nibh. Aenean vitae odio ac risus aliquam malesuada. Quisque mollis mauris quis odio bibendum consectetur. Vestibulum venenatis odio dolor, nec pretium odio.</p>
<div class="photo owners" role="img" aria-label="Partners holding a framed award plaque"></div>
<a class="btn" href="#" style="left:105px;top:646px;width:72px">Read More</a>

<div class="hrule abs"></div>
<div class="vrule abs"></div>

<h2 style="left:103px;top:705px">WELCOME TO COF PARTNERS.COM</h2>
<div class="photo race" role="img" aria-label="Chestnut racehorse and jockey racing under lights"></div>
<p class="copy" style="left:103px;top:903px;width:336px">Lorem ipsum dolor sit amet, consectetur adipiscing elit. Curabitur eget nibh id enim laoreet euismod eget ac orci. Vestibulum anipsum primis in faucibus orci luctus. et ultrices posuere cubilia Curae; Cras pellentesque euismod fringilla. Sed vitae ante lectus, non fringilla nibh. Aenean vitae odio ac risus aliquam malesuada. Quisque mollis mauris quis odio bibendum consectetur. Vestibulum venenatis odio dolor, nec pretium odio. quis dolor sapien, et gravida mauris.</p>
<a class="btn" href="#" style="left:103px;top:1031px;width:79px">Read More</a>

<h2 style="left:494px;top:705px">LATEST NEWS</h2>
<article class="news-item" style="top:759px"><h3>08 November, 2013</h3><p>Lorem ipsum dolor sit amet, consectetur adipiscing elit. Curabitur eget nibh id enim laoreet euismod</p><a href="#">posted by Lorem ipsum</a></article>
<article class="news-item" style="top:847px"><h3>06 November, 2013</h3><p>Lorem ipsum dolor sit amet, consectetur adipiscing elit. Curabitur eget nibh id enim laoreet euismod</p><a href="#">posted by Lorem ipsum</a></article>
<article class="news-item" style="top:932px"><h3>04 November, 2013</h3><p>Lorem ipsum dolor sit amet, consectetur adipiscing elit. Curabitur eget nibh id enim laoreet euismod</p><a href="#">posted by Lorem ipsum</a></article>
<a class="btn" href="#" style="left:493px;top:1027px;width:79px">Read More</a>

<footer>
  <p class="footer-nav abs"><a href="#">Home</a><i>|</i><a href="#">About Us</a><i>|</i><a href="#">Ownership</a><i>|</i><a href="#">Stable Roster</a><i>|</i><a href="#">News</a><i>|</i><a href="#">Contact us</a></p>
  <p class="copyright abs">© Copyright 2013 - All rights reserved.</p>
  <div class="social bottom abs"><span></span><span></span><span></span><span></span></div>
</footer>

</body>
</html>
```